For our annual dance recital this year we will have an asylum/ orphans/ any spooky shelter. Thats the feel of it.
i will be need an invitation and a ticket.
as the recital will be done in two days the tickets will have same design but different colors.
My idea is to have spooky fonts/ x ray images somehow put in the design.
i will be uploading a lot of images for you to understand where i would like to take this design.
for the invitation i do want to have part of the paper printed in see through material like some of the images uploaded or have an x-ray effect.
the invitation should have this written on it.
MORVANE
Our production is ready and we are dying to have you around. So crawl on over for a spooktacular happening at
IBN TAMRIQ UNIVERSITY AUDITORIUM
The undertaking will begin from 1:30pm to 3:30pm
May 2nd 2014 and May 3rd 2014
The entry tickets will be two colors but same design. i would like it to be printed of see through plastic paper. so we can have one see through and font in black and the other one is dark see through written in white maybe. please make in an xray effext with maybe the pointed feet picture somehow incorporated in the design
i want it to look like the picture i uploaded of (Corbys 4th birthday) in regard of layout of the writings i like how the date is stamped and i like how the date is pointed out in a dot.
here what to write on tickets
The name of the recital
Issued by Veluzzo
MORVANE
(Find me a sentence that means admit one)
we do need numbers as the seats are numbered
so all in all i would like the invitation and ticket to go together i was thinking of having the dancer bridge xray on invitation and the pointed feet on the ticket.
if you have any other nice parts of the body xray that somehow show its a dancer im also open to that.
than main idea is to have a nice design that is so creative yet simple. play with the fonts to deliver this spooky feeling but all with elegance.
please notice that the picture with the person smoking Xray .. i like how its black and the words are see through with the xray picture. so this would be nice as an idea.
Reason: I still did not find a design that i like.
the theme is asylum. i want it creepy but in the same time ELEGANT. I will be printing invitation on CLEAR paper so the X ray picture could be incorporated in the design in a very subtle way.
Please ask me any question if its not clear
PS my budget is higher now.

```html
<!DOCTYPE html>
<html lang="en">
<head>
<meta charset="utf-8">
<title>Morvane – Invitation</title>
<link rel="stylesheet" href="https://fonts.googleapis.com/css2?family=Londrina+Outline&family=Questrial&family=Montserrat:wght@500;600&display=swap">
<style>
  :root {
    --page: #f4f4f2;
    --card: #050505;
    --xray-yellow: #f2e20a;
    --ink-yellow: #f5d90f;
    --ink-white: #ffffff;
    --bone: #e8e8dc;
  }
  * { box-sizing: border-box; margin: 0; padding: 0; }
  html, body {
    width: 1200px; height: 726px; overflow: hidden;
    background: var(--page);
  }
  .invitation-card {
    position: absolute; left: 50px; top: 78px;
    width: 1100px; height: 570px;
    background: var(--card);
    box-shadow: inset -30px 0 40px -20px rgba(255,255,255,0.18),
                inset 0 -20px 30px -20px rgba(255,255,255,0.12);
    overflow: hidden;
  }
  .xray-dancer {
    position: absolute; left: 20px; top: 20px;
    width: 400px; height: 500px;
    background:
      radial-gradient(ellipse 38% 30% at 30% 40%, rgba(242,226,10,0.75), rgba(242,226,10,0) 70%),
      radial-gradient(ellipse 40% 14% at 55% 12%, rgba(242,226,10,0.55), rgba(242,226,10,0) 70%),
      radial-gradient(ellipse 18% 30% at 72% 62%, rgba(242,226,10,0.5), rgba(242,226,10,0) 70%),
      radial-gradient(ellipse 30% 14% at 25% 85%, rgba(232,232,220,0.45), rgba(232,232,220,0) 70%);
  }
  .card-copy {
    position: absolute; left: 430px; top: 70px; width: 640px;
  }
  .recital-title {
    font-family: "Londrina Outline", cursive;
    font-weight: 400;
    font-size: 142px; line-height: 1;
    letter-spacing: 4px;
    color: var(--ink-yellow);
  }
  .recital-title .last-letter { color: var(--ink-white); }
  .welcome-text {
    margin-top: 14px;
    font-family: "Questrial", sans-serif;
    font-size: 21px; line-height: 1.33;
    color: var(--ink-yellow);
  }
  .venue { display: block; }

  .date-strip {
    position: absolute; left: 430px; top: 375px;
    display: flex; height: 60px;
    border: 2px solid var(--ink-white);
  }
  .date-cell {
    width: 40px;
    border-right: 2px solid var(--ink-white);
    display: flex; align-items: center; justify-content: center;
    font-family: "Montserrat", sans-serif; font-weight: 500;
    color: var(--ink-white);
    position: relative;
  }
  .date-cell:last-child { border-right: none; }
  .date-cell.year { width: 48px; font-weight: 600; font-size: 18px; }
  .month {
    writing-mode: vertical-rl; transform: rotate(180deg);
    font-size: 15px; letter-spacing: 1px;
  }
  .month.is-marked::after {
    content: ""; position: absolute;
    width: 16px; height: 16px; border-radius: 50%;
    background: var(--ink-white);
    left: 50%; top: 50%; transform: translate(-50%, -50%);
  }
  .day-row {
    position: absolute; left: 430px; top: 455px;
    display: flex; gap: 4px;
    font-family: "Montserrat", sans-serif; font-weight: 500;
    font-size: 13.5px; color: var(--ink-white);
  }
  .day.is-marked {
    display: inline-block; width: 12px; height: 12px; margin-top: 3px;
    border-radius: 50%; background: var(--ink-white);
    color: transparent; overflow: hidden;
  }
  .schedule {
    position: absolute; left: 490px; top: 488px;
    font-family: "Montserrat", sans-serif; font-weight: 500;
    font-size: 18px; color: var(--ink-white);
  }
</style>
</head>
<body>
  <main class="invitation-card">
    <div class="xray-dancer" role="img" aria-label="Glowing yellow x-ray of a dancer's skeleton in a backbend bridge, wearing a tutu"></div>

    <section class="card-copy">
      <h1 class="recital-title">MORVAN<span class="last-letter">E</span></h1>
      <p class="welcome-text">
        Our production is ready and we are dying to have you around. So crawl on over for a spooktacular happening at
        <span class="venue">IBN TAMRIQ UNIVERSITY AUDITORIUM</span>
      </p>
    </section>

    <div class="date-strip">
      <div class="date-cell year">20</div>
      <div class="date-cell"><span class="month">JAN</span></div>
      <div class="date-cell"><span class="month">FEB</span></div>
      <div class="date-cell"><span class="month">MAR</span></div>
      <div class="date-cell"><span class="month">APR</span></div>
      <div class="date-cell"><span class="month is-marked">MAY</span></div>
      <div class="date-cell"><span class="month">JUN</span></div>
      <div class="date-cell"><span class="month">AUG</span></div>
      <div class="date-cell"><span class="month">SEP</span></div>
      <div class="date-cell"><span class="month">OCT</span></div>
      <div class="date-cell"><span class="month">NOV</span></div>
      <div class="date-cell"><span class="month">DEC</span></div>
      <div class="date-cell year">14</div>
    </div>

    <div class="day-row">
      <span class="day">1</span><span class="day is-marked">2</span><span class="day is-marked">3</span><span class="day">4</span><span class="day">5</span><span class="day">6</span><span class="day">7</span><span class="day">8</span><span class="day">9</span><span class="day">10</span><span class="day">11</span><span class="day">12</span><span class="day">13</span><span class="day">14</span><span class="day">15</span><span class="day">16</span><span class="day">17</span><span class="day">18</span><span class="day">19</span><span class="day">20</span><span class="day">21</span><span class="day">22</span><span class="day">23</span><span class="day">24</span><span class="day">25</span><span class="day">26</span><span class="day">27</span><span class="day">28</span><span class="day">29</span><span class="day">30</span><span class="day">31</span>
    </div>

    <p class="schedule">The undertaking will begin from 1:30pm to 3:30pm</p>
  </main>
</body>
</html>
```